Occupational Therapist does home accessibility for disabled folks; needs business card design

We need a business card for a company in Portland, Oregon that specializes in making homes accessible, comfortable, and functional for people who are disabled or aging who would like to stay in THEIR home. Our medical background as Occupational Therapists allows us to translate the functional needs of the person into the recommendations for the design of the home remodel.

Target Market(s)

Elderly, children of elderly
People with disabilities, families of people with disabilities

Industry/Entity Type

Business

Contact Information for Business Card

Company name: HomeWise
Name: Danielle Reyes Crawford, OTR/L, CAPS, ECHM
Occupational Therapist, Home Modification & Accessibility Specialist
website: www.homewiseforyears.com
email: homewiseforyears@nestmail.example
phone: (503)218-4057
CCB #: 487315

Font styles to use
Sans Serif

Requirements
Must have
• My logo
• Easy to read font with contrasting background
• Please list the Services offered: Occupational Therapy, Home safety & accessibility assessments, Home modification consulting, project management
Nice to have
• Friendly, welcoming feel
Should not have
• Dark colored background

```html
<!DOCTYPE html>
<html lang="en">
<head>
<meta charset="utf-8">
<title>HomeWise Business Card</title>
<link href="https://fonts.googleapis.com/css2?family=Roboto:wght@400;500&family=Fira+Sans+Condensed:wght@500&display=swap" rel="stylesheet">
<style>
  :root {
    --backdrop: #e6e6e4;
    --card-white: #ffffff;
    --card-grey: #666666;
    --accent-orange: #d07f19;
    --ink-grey: #5b5b5b;
    --text-grey: #555555;
    --rule-grey: #cfcfcf;
    --white: #ffffff;
  }
  * { box-sizing: border-box; margin: 0; padding: 0; }
  html, body {
    width: 1105px; height: 1200px; overflow: hidden;
    background: var(--backdrop);
    font-family: "Roboto", Arial, sans-serif;
  }
  .card {
    position: absolute; left: 196px; width: 720px; height: 410px;
    overflow: hidden;
    box-shadow: 0 3px 10px rgba(0,0,0,0.18);
  }
  .card-front { top: 146px; background: var(--card-white); }
  .card-back { top: 602px; background: var(--card-grey); }

  .brand-lockup {
    position: absolute; left: 50px; top: 150px; width: 290px;
    display: flex; align-items: center; gap: 12px;
  }
  .brand-mark { width: 28px; height: 28px; background: var(--ink-grey); flex: none; }
  .brand-name {
    font-family: "Fira Sans Condensed", "Roboto", sans-serif;
    font-weight: 500; font-size: 54px; line-height: 1;
    color: var(--accent-orange); white-space: nowrap;
  }
  .divider {
    position: absolute; left: 365px; top: 75px; width: 1px; height: 227px;
    background: var(--rule-grey);
  }
  .contact-block {
    position: absolute; left: 395px; top: 80px; width: 310px;
    color: var(--text-grey); white-space: nowrap;
  }
  .person-name {
    font-weight: 500; font-size: 21px; letter-spacing: 0.2px;
    color: var(--accent-orange); text-transform: uppercase;
  }
  .person-credentials {
    font-weight: 500; font-size: 16px; color: var(--accent-orange); margin-top: 3px;
  }
  .person-role {
    font-size: 17px; line-height: 24px; text-transform: uppercase; margin-top: 12px;
  }
  .contact-list { list-style: none; margin-top: 12px; font-size: 17px; line-height: 28px; }
  .contact-list li { display: flex; align-items: center; gap: 8px; }
  .contact-list .email { font-size: 16px; }
  .contact-list svg { width: 15px; height: 15px; fill: var(--accent-orange); flex: none; }
  .web-band {
    position: absolute; left: 0; top: 354px; width: 100%; height: 30px;
    background: var(--accent-orange);
    color: var(--white); font-size: 17px; letter-spacing: 3px;
    display: flex; align-items: center; justify-content: center;
  }

  .back-lockup {
    position: absolute; left: 0; top: 120px; width: 100%;
    display: flex; justify-content: center; align-items: center; gap: 16px;
  }
  .back-lockup .brand-mark { background: var(--white); width: 34px; height: 34px; }
  .back-lockup .brand-name { color: var(--white); font-size: 76px; }
  .services {
    position: absolute; left: 0; top: 290px; width: 100%; text-align: center;
    color: var(--white);
  }
  .services-title {
    font-weight: 500; font-size: 23px; color: var(--accent-orange); margin-bottom: 8px;
  }
  .services-line { font-size: 19px; line-height: 27px; }
  .services-line .sep {
    display: inline-block; width: 7px; height: 7px; background: var(--white);
    margin: 0 9px 3px; vertical-align: middle;
  }
</style>
</head>
<body>
  <section class="card card-front">
    <div class="brand-lockup">
      <span class="brand-mark"></span>
      <span class="brand-name">HomeWise</span>
    </div>
    <div class="divider"></div>
    <div class="contact-block">
      <h1 class="person-name">Danielle Reyes Crawford</h1>
      <p class="person-credentials">OTR/L, CAPS, ECHM</p>
      <p class="person-role">Occupational Therapist<br>Home Modification &amp;<br>Accessibility Specialist</p>
      <ul class="contact-list">
        <li><svg viewBox="0 0 24 24" aria-hidden="true"><path d="M6.6 10.8a15.1 15.1 0 0 0 6.6 6.6l2.2-2.2a1 1 0 0 1 1-.25 11.4 11.4 0 0 0 3.6.57 1 1 0 0 1 1 1V20a1 1 0 0 1-1 1A17 17 0 0 1 3 4a1 1 0 0 1 1-1h3.5a1 1 0 0 1 1 1c0 1.25.2 2.45.57 3.57a1 1 0 0 1-.25 1z"/></svg>(503)218-4057</li>
        <li class="email"><svg viewBox="0 0 24 24" aria-hidden="true"><path d="M2 5h20v14H2z"/><path d="M3 6l9 7 9-7" fill="none" stroke="#fff" stroke-width="1.6"/></svg>homewiseforyears@nestmail.example</li>
        <li>CCB #: 487315</li>
      </ul>
    </div>
    <div class="web-band">www.homewiseforyears.com</div>
  </section>

  <section class="card card-back">
    <div class="back-lockup">
      <span class="brand-mark"></span>
      <span class="brand-name">HomeWise</span>
    </div>
    <div class="services">
      <h2 class="services-title">Services</h2>
      <p class="services-line">Occupational Therapy<span class="sep"></span>Home safety &amp; accessibility assessments</p>
      <p class="services-line">Home modification consulting<span class="sep"></span>Project management</p>
    </div>
  </section>
</body>
</html>
```